Morrow & Pellant Stationery

Greetings again. Now we've got an awesome logo, it's time to get the stationery to go with it. We require the following items of stationery:

- Business Card - Print Ready, all we need to do is change names and numbers and submit to printer.  Double sided with logo on one side and details on the other side. (85mm x 55mm)

- With Compliments Slip

- Letterhead - These will be preprinted pages that will then be used as pages.
(A4)

- Envelope - Business Size(Standard DL)

Target Market(s)

Essentially, this firm services clients facing criminal charges and/or seeking legal aid. The firm is also looking at taking on more white-collar crime cases.

Requirements
Must have
• - Same Design Cues & Colours as the Branding details attached

• - Address (as follows)

• Suite 8

• 212-216 Carrow St

• HARLOWE VIC 3999

• Phone: (03) 9555 0142

• Fax: (03) 9555 0187

• Web: www.morrowandpellant.example

• - Colour: Pantone 194 (Red)

```html
<!DOCTYPE html>
<html lang="en">
<head>
<meta charset="utf-8">
<title>Morrow &amp; Pellant Stationery</title>
<link href="https://fonts.googleapis.com/css2?family=Cinzel:wght@500;600&family=Tinos:ital,wght@0,400;0,700;1,400&display=swap" rel="stylesheet">
<style>
  :root {
    --brand-red: #8e2237;
    --paper: #ffffff;
    --ink: #111111;
    --ink-soft: #444444;
    --backdrop: #000000;
  }
  * { box-sizing: border-box; margin: 0; padding: 0; }
  html, body {
    width: 1200px; height: 845px; overflow: hidden;
    background: var(--backdrop);
  }
  .sheet { position: relative; width: 1200px; height: 845px; }

  .piece { position: absolute; overflow: hidden; background: var(--brand-red); }
  .piece > svg.backdrop { position: absolute; inset: 0; width: 100%; height: 100%; }
  .piece .content { position: absolute; inset: 0; }

  .card-front { left: 54px; top: 43px; width: 231px; height: 148px; }
  .card-back  { left: 337px; top: 43px; width: 231px; height: 148px; }
  .comp-slip  { left: 27px; top: 217px; width: 569px; height: 270px; }
  .envelope   { left: 12px; top: 515px; width: 597px; height: 298px; }
  .letterhead { left: 619px; top: 29px; width: 568px; height: 805px; }

  /* brand lockup */
  .brand { position: absolute; display: flex; align-items: center; }
  .brand-mark { border-radius: 50%; background: var(--brand-red); flex: none; }
  .brand-text { display: flex; flex-direction: column; line-height: 1; }
  .brand-name {
    font-family: "Cinzel", serif; font-weight: 600; color: var(--ink);
    white-space: nowrap;
  }
  .brand-tagline {
    font-family: "Cinzel", serif; font-weight: 600; color: var(--ink-soft);
    white-space: nowrap; letter-spacing: 0.03em;
  }

  .card-front .brand { left: 13px; top: 48px; }
  .card-front .brand-mark { width: 51px; height: 51px; margin-right: 18px; }
  .card-front .brand-name { font-size: 13.5px; }
  .card-front .brand-tagline { font-size: 7.5px; margin-top: 2px; }

  .letterhead .brand { left: 150px; top: 48px; }
  .letterhead .brand-mark { width: 67px; height: 67px; margin-right: 26px; }
  .letterhead .brand-name { font-size: 19px; }
  .letterhead .brand-tagline { font-size: 10.5px; margin-top: 3px; }

  .comp-slip .brand, .envelope .brand { left: 14px; top: 14px; }
  .comp-slip .brand-mark, .envelope .brand-mark { width: 41px; height: 41px; margin-right: 14px; }
  .comp-slip .brand-name, .envelope .brand-name { font-size: 12px; }
  .comp-slip .brand-tagline, .envelope .brand-tagline { font-size: 6.5px; margin-top: 2px; }

  /* text blocks */
  .contact {
    position: absolute; left: 0; right: 0; text-align: center;
    font-family: "Tinos", serif; color: var(--ink); line-height: 1.45;
  }
  .contact .sep { color: var(--ink-soft); margin: 0 4px; }

  .card-back .holder {
    position: absolute; left: 0; right: 0; top: 43px; text-align: center;
    font-family: "Tinos", serif; color: var(--ink);
  }
  .card-back .holder-name { font-size: 21px; line-height: 1; }
  .card-back .holder-role { font-size: 11px; color: var(--ink-soft); margin-top: 2px; }
  .card-back .contact { top: 101px; font-size: 8px; color: var(--ink-soft); }

  .comp-slip .greeting {
    position: absolute; left: 0; right: 0; top: 63px; padding-left: 26px;
    text-align: center; font-family: "Tinos", serif; font-style: italic;
    font-size: 19px; color: var(--ink-soft);
  }
  .comp-slip .contact { top: 222px; font-size: 8.5px; font-weight: 700; }

  .envelope .return-address {
    position: absolute; left: 71px; top: 60px;
    font-family: "Tinos", serif; font-style: normal;
    font-size: 11.5px; line-height: 1.3; color: var(--ink);
  }

  .letterhead .contact { top: 746px; font-size: 10.5px; }
  .letterhead .contact .sep { margin: 0 12px; }
</style>
</head>
<body>
<main class="sheet">

  <section class="piece card-front" aria-label="Business card front">
    <svg class="backdrop" viewBox="0 0 231 148" preserveAspectRatio="none" aria-hidden="true">
      <ellipse cx="114" cy="74" rx="130" ry="110" fill="var(--paper)"/>
    </svg>
    <div class="content">
      <div class="brand">
        <span class="brand-mark"></span>
        <span class="brand-text">
          <span class="brand-name">Morrow &amp; Pellant</span>
          <span class="brand-tagline">Barristers &amp; Solicitors</span>
        </span>
      </div>
    </div>
  </section>

  <section class="piece card-back" aria-label="Business card back">
    <svg class="backdrop" viewBox="0 0 231 148" preserveAspectRatio="none" aria-hidden="true">
      <ellipse cx="117" cy="74" rx="130" ry="110" fill="var(--paper)"/>
    </svg>
    <div class="content">
      <div class="holder">
        <p class="holder-name">Jamie Lee Hart</p>
        <p class="holder-role">Professional Name Holder</p>
      </div>
      <div class="contact">
        <p>Suite 8<span class="sep">|</span>212-216 Carrow St<span class="sep">|</span>HARLOWE VIC 3999</p>
        <p>Phone: (03) 9555 0142<span class="sep">|</span>Fax: (03) 9555 0187</p>
        <p>Web: www.morrowandpellant.example</p>
      </div>
    </div>
  </section>

  <section class="piece comp-slip" aria-label="With compliments slip">
    <svg class="backdrop" viewBox="0 0 569 270" preserveAspectRatio="none" aria-hidden="true">
      <ellipse cx="284" cy="-46" rx="405" ry="318" fill="var(--paper)"/>
    </svg>
    <div class="content">
      <div class="brand">
        <span class="brand-mark"></span>
        <span class="brand-text">
          <span class="brand-name">Morrow &amp; Pellant</span>
          <span class="brand-tagline">Barristers &amp; Solicitors</span>
        </span>
      </div>
      <p class="greeting">With our compliments</p>
      <div class="contact">
        <p>Suite 8<span class="sep">|</span>212-216 Carrow St<span class="sep">|</span>HARLOWE VIC 3999</p>
        <p>Phone: (03) 9555 0142<span class="sep">|</span>Fax: (03) 9555 0187</p>
        <p>Web: www.morrowandpellant.example</p>
      </div>
    </div>
  </section>

  <section class="piece envelope" aria-label="DL envelope">
    <svg class="backdrop" viewBox="0 0 597 298" preserveAspectRatio="none" aria-hidden="true">
      <ellipse cx="298" cy="0" rx="308" ry="340" fill="var(--paper)"/>
    </svg>
    <div class="content">
      <div class="brand">
        <span class="brand-mark"></span>
        <span class="brand-text">
          <span class="brand-name">Morrow &amp; Pellant</span>
          <span class="brand-tagline">Barristers &amp; Solicitors</span>
        </span>
      </div>
      <address class="return-address">
        Suite 8<br>212-216 Carrow St<br>HARLOWE VIC 3999
      </address>
    </div>
  </section>

  <section class="piece letterhead" aria-label="A4 letterhead">
    <svg class="backdrop" viewBox="0 0 568 805" preserveAspectRatio="none" aria-hidden="true">
      <ellipse cx="284" cy="402" rx="420" ry="415" fill="var(--paper)"/>
    </svg>
    <div class="content">
      <div class="brand">
        <span class="brand-mark"></span>
        <span class="brand-text">
          <span class="brand-name">Morrow &amp; Pellant</span>
          <span class="brand-tagline">Barristers &amp; Solicitors</span>
        </span>
      </div>
      <div class="contact">
        <p>Suite 8<span class="sep">|</span>212-216 Carrow St<span class="sep">|</span>HARLOWE VIC 3999</p>
        <p>Phone: (03) 9555 0142<span class="sep">|</span>Fax: (03) 9555 0187</p>
        <p>www.morrowandpellant.example</p>
      </div>
    </div>
  </section>

</main>
</body>
</html>
```